Do it yourself Karten und Hochzeitsdeko selbstgemacht
Zielgruppe
Wir sind ein Bastelgeschäft. Wir bieten Materialien zum selber machen von Karten, Tischkarten,Menükarten, Gästebüchern, Fotoalben an.
Alle Materialien zur Anlassgestaltung, auch Tischdeko und Kerzen.
Zielgruppe: Junge Leute auf einer Hochzeitsmesse
Aufgabenstellung
Ich benötige einen Flyer in A5 Format. Einige Fotoausschnitte und Text. Romantisch.
Fotos von angefertigten Karten und Deko sind vorhanden.
Logo vorhanden, soll mit rein und Öffnungszeiten mit Internet
Text: Do it Yourself Karten und Hochzeitsdeko selbst gemacht!
Zeiten etc. bitte www.falten-und-schmuecken.de

```html
<!DOCTYPE html>
<html lang="de">
<head>
<meta charset="utf-8">
<title>Lindner Basteln &amp; Dekorieren – Flyer</title>
<link href="https://fonts.googleapis.com/css2?family=Roboto+Condensed:wght@300;400;700&family=Great+Vibes&display=swap" rel="stylesheet">
<style>
  :root{
    --teal:#5e939b;
    --teal-dark:#3f6c73;
    --ink:#355a60;
    --paper:#ffffff;
    --frame:#ffffff;
    --photo-light:#dfe2e6;
    --photo-mid:#c9ced4;
    --leaf:#5c7a5c;
  }
  *{margin:0;padding:0;box-sizing:border-box}
  html,body{width:1200px;height:848px;overflow:hidden;background:#fff}
  body{position:relative;font-family:"Roboto Condensed",Arial,sans-serif;color:var(--ink)}
  .page{position:absolute;top:118px;width:423px;height:600px;background:var(--paper);box-shadow:0 1px 4px rgba(0,0,0,.25);overflow:hidden}
  .page--front{left:134px}
  .page--back{left:644px}
  .band{position:absolute;left:0;right:0;top:200px;bottom:0;background:var(--teal)}
  .photo{position:absolute;border:2px solid var(--frame)}
  .photo--cards{left:39px;top:216px;width:344px;height:245px;background:linear-gradient(135deg,var(--photo-mid),var(--photo-light) 55%,#eceef0)}
  .stamp{position:absolute;width:106px;height:106px;border-radius:50%;background:var(--teal);border:3px solid #fff;box-shadow:0 0 0 2px var(--teal);display:flex;align-items:center;justify-content:center;color:#fff;font-weight:300;font-size:22px}
  .page--front .stamp{left:304px;top:374px}
  .page--back .stamp{left:158px;top:345px}
  .brand{position:absolute;left:0;right:0;top:36px;text-align:center;color:var(--teal-dark)}
  .brand__name{font-size:56px;font-weight:300;line-height:1;letter-spacing:1px}
  .brand__sub{font-size:20px;font-weight:400;color:#4a4f52;margin-top:2px}
  .headline{position:absolute;left:0;top:133px;width:423px;font-weight:700;font-size:21px;line-height:24px;color:var(--ink)}
  .headline__line{display:block}
  .headline__line--one{text-align:center}
  .headline__line--two{padding-left:94px}
  .headline__script{position:absolute;left:226px;top:156px;font-family:"Great Vibes",cursive;font-size:30px;color:var(--ink);transform:rotate(-12deg);font-weight:400;white-space:nowrap}
  .offer__title{position:absolute;left:38px;top:470px;font-family:"Great Vibes",cursive;font-size:20px;color:#fff}
  .offer__list{position:absolute;top:502px;list-style:none;color:#fff;font-weight:300;font-size:9.2px;line-height:12px}
  .offer__list li{padding-left:6px;text-indent:-6px}
  .offer__list li::before{content:"• "}
  .offer__list--a{left:33px;width:180px}
  .offer__list--b{left:227px;width:165px}
  .info{position:absolute;left:0;right:0;top:22px;text-align:center;font-size:9.6px;line-height:12px;font-weight:300;color:var(--ink)}
  .info strong{font-weight:700}
  .info p{margin-bottom:4px}
  .info .web{font-weight:700;font-size:10px}
  .quote{position:absolute;left:30px;right:30px;top:149px;text-align:center;color:var(--teal);font-weight:700;font-size:14px;line-height:16px}
  .grid{position:absolute;left:40px;top:216px;width:343px;height:367px;background:#fff}
  .cell{position:absolute}
  .cell--tl{left:2px;top:2px;width:168px;height:119px;background:linear-gradient(135deg,var(--photo-mid),var(--photo-light))}
  .cell--r{left:173px;top:2px;width:168px;height:242px;background:radial-gradient(circle at 40% 55%,var(--leaf),#b9c2c0 45%,var(--photo-light))}
  .cell--bl{left:2px;top:124px;width:168px;height:241px;background:radial-gradient(circle at 45% 65%,var(--leaf),#d7dad8 40%,#e9eae6)}
  .cell--br{left:173px;top:247px;width:168px;height:118px;background:linear-gradient(120deg,var(--photo-mid),#e6e8ea)}
</style>
</head>
<body>

<section class="page page--front">
  <div class="brand">
    <div class="brand__name">Lindner</div>
    <div class="brand__sub">Basteln &amp; Dekorieren</div>
  </div>
  <h1 class="headline">
    <span class="headline__line headline__line--one">DO-IT-YOURSELF-KARTEN UND</span>
    <span class="headline__line headline__line--two">HOCHZEITSDEKO</span>
  </h1>
  <div class="headline__script">selbst gemacht!</div>
  <div class="band"></div>
  <div class="photo photo--cards" role="img" aria-label="Foto: weiße Hochzeitskarten mit gestanzten Herzen, Schleifen und Serviette"></div>
  <div class="stamp">Lindner</div>
  <div class="offer__title">In unseren Räumen finden Sie:</div>
  <ul class="offer__list offer__list--a">
    <li>Herziges und Glückbringendes, Brautpaare, Tauben, Ringkissen, Fotoalben, Gästebücher, Kerzen und Servietten.</li>
    <li>Auswahl verschiedenster Papiere und Stempel, zur Kartengestaltung für Hochzeit, Taufe, Konfirmation, Geburtstag und sonstige Anlässe.</li>
    <li>Wachsplatten und Stifte zum Kerzen verzieren.</li>
  </ul>
  <ul class="offer__list offer__list--b">
    <li>Verschiedene Variationen von Bändern, Kordeln und Tüll für Kirchendekorationen und Autoschmuck.</li>
    <li>Glas- und Wachsperlen, Pailetten, Rocailles und Indianerperlen, Straßsteine und Glitzerkristalle, Drähte, Verschlüsse und Bänder zur Schmuckgestaltung.</li>
  </ul>
</section>

<section class="page page--back">
  <div class="info">
    <p><strong>Öffnungszeiten:</strong><br>Mo., Di., Do. und Fr.: 9.00 Uhr – 12.30 Uhr und 14.00 Uhr – 18.30 Uhr<br>Mi. und Sa.: 9.00 Uhr – 13.30 Uhr</p>
    <p><strong>Kontakt:</strong><br>Lindner Basteln und Dekorieren | Gartenweg 12 | 24103 Kiel<br>Telefon: 0431.552870 | Telefax: 0431.55 28 71<br>info@falten-und-schmuecken.de</p>
    <p class="web">www.falten-und-schmuecken.de</p>
  </div>
  <p class="quote">“Wir würden uns freuen, Sie bei der Gestaltung Ihrer ganz persönlichen Einladungskarte beraten zu dürfen.”</p>
  <div class="band"></div>
  <div class="grid">
    <div class="cell cell--tl" role="img" aria-label="Foto: Karte mit Herz und Serviettenrolle"></div>
    <div class="cell cell--r" role="img" aria-label="Foto: Glas mit grünem Blätterkranz und Schleife"></div>
    <div class="cell cell--bl" role="img" aria-label="Foto: Karte mit grünem Herzkranz und weißer Schleife"></div>
    <div class="cell cell--br" role="img" aria-label="Foto: Menükarte neben einem Glas"></div>
  </div>
  <div class="stamp">Lindner</div>
</section>

</body>
</html>
```